Love pets? Create a veterinary business card that aligns with our new revamped website.

Greetings! We are a five-doctor veterinary hospital that seeks your expertise in designing a new business card that harmonizes with our recently revitalized website: www.tqrn.net. The card should feature our logo, the five doctors, operating hours, contact information, and communicate our purpose and personality.

Contact Information for Business Card

TBA

```html
<!DOCTYPE html>
<html lang="en">
<head>
<meta charset="utf-8">
<title>Maple Hollow Veterinary Hospital – Business Card</title>
<link rel="stylesheet" href="https://fonts.googleapis.com/css2?family=Montserrat:wght@600;800&family=Open+Sans:wght@400;600&display=swap">
<style>
  :root{
    --backdrop:#4a4a49;
    --card:#ffffff;
    --green:#4a8d3f;
    --brown:#7d5a1e;
    --ink:#2b2b2b;
  }
  *{box-sizing:border-box;margin:0;padding:0}
  html,body{width:1200px;height:801px;overflow:hidden}
  body{background:var(--backdrop);position:relative;font-family:"Open Sans",sans-serif;color:var(--ink)}
  .card{
    position:absolute;top:246px;width:540px;height:309px;
    background:var(--card);border-bottom:3px solid var(--green);border-right:3px solid var(--green);
    box-shadow:0 14px 30px rgba(0,0,0,.35);
  }
  .card--info{left:40px}
  .card--brand{left:620px}

  /* info side */
  .brand-mark{display:flex;align-items:center;gap:8px;position:absolute;left:36px;top:30px}
  .brand-mark__dot{width:14px;height:14px;border-radius:50%;background:var(--green)}
  .brand-mark__name{font-family:"Montserrat",sans-serif;font-weight:600;font-size:13px;color:var(--green);line-height:1.15}
  .accent-bar{position:absolute;left:0;top:104px;width:26px;height:40px;background:var(--green)}
  .person{position:absolute;left:40px;top:100px}
  .person__name{font-family:"Montserrat",sans-serif;font-weight:800;font-size:20px;color:var(--green);letter-spacing:.5px}
  .person__role{font-size:13px;margin-top:1px}
  .contacts{list-style:none;position:absolute;left:40px;top:160px;font-size:12.5px;line-height:19px}
  .contacts li{display:flex;align-items:center;gap:7px}
  .contacts svg{width:12px;height:12px;fill:var(--green);flex:none}
  .address{position:absolute;left:40px;top:246px;display:flex;gap:7px;font-size:12.5px;line-height:17px}
  .address svg{width:12px;height:14px;fill:var(--green);flex:none;margin-top:2px}
  .doctors{list-style:none;position:absolute;right:30px;top:150px;text-align:right;
    font-family:"Montserrat",sans-serif;font-weight:800;font-size:15.5px;line-height:25px;color:var(--green);letter-spacing:.4px}

  /* brand side */
  .brand-lockup{position:absolute;inset:0;display:flex;align-items:center;justify-content:center;gap:14px}
  .brand-lockup__dot{width:46px;height:46px;border-radius:50%;background:var(--green)}
  .brand-lockup__name{font-family:"Montserrat",sans-serif;font-weight:600;font-size:30px;line-height:1.1;color:var(--green)}
</style>
</head>
<body>

<section class="card card--info">
  <div class="brand-mark">
    <span class="brand-mark__dot"></span>
    <span class="brand-mark__name">Maple Hollow<br>Veterinary Hospital</span>
  </div>

  <div class="accent-bar"></div>
  <div class="person">
    <p class="person__name">DAN PORTER</p>
    <p class="person__role">Managing Director</p>
  </div>

  <ul class="contacts">
    <li><svg viewBox="0 0 24 24"><path d="M6.6 10.8a15 15 0 0 0 6.6 6.6l2.2-2.2a1 1 0 0 1 1-.25 11.4 11.4 0 0 0 3.6.57 1 1 0 0 1 1 1V20a1 1 0 0 1-1 1A17 17 0 0 1 3 4a1 1 0 0 1 1-1h3.5a1 1 0 0 1 1 1c0 1.25.2 2.45.57 3.57a1 1 0 0 1-.25 1z"/></svg>(555) 214-0187</li>
    <li><svg viewBox="0 0 24 24"><path d="M6 2h10v5H6zM3 8h18v11H3zM6 14h12v8H6z"/></svg>(555) 362-4410</li>
    <li><svg viewBox="0 0 24 24"><path d="M2 5h20v14H2zm2 2v.5l8 5 8-5V7l-8 5z"/></svg>info@tqrn.net</li>
    <li><svg viewBox="0 0 24 24"><circle cx="12" cy="12" r="10"/></svg>www.tqrn.net</li>
  </ul>

  <div class="address">
    <svg viewBox="0 0 24 28"><path d="M12 0a9 9 0 0 0-9 9c0 7 9 19 9 19s9-12 9-19a9 9 0 0 0-9-9zm0 13a4 4 0 1 1 0-8 4 4 0 0 1 0 8z"/></svg>
    <p>2480 Cedar Ridge Road,<br>Millbrook, TX 75021</p>
  </div>

  <ul class="doctors">
    <li>RAY HOLDEN, DVM</li>
    <li>JANE MERCER, DVM</li>
    <li>LAURA FINCH, DVM</li>
    <li>CAROLINE PARK, DVM</li>
  </ul>
</section>

<section class="card card--brand">
  <div class="brand-lockup">
    <span class="brand-lockup__dot"></span>
    <span class="brand-lockup__name">Maple Hollow<br>Veterinary Hospital</span>
  </div>
</section>

</body>
</html>
```